Baby Boutique Needs a Business Card Design

We need a modern double sided business card design using the attached logo for L' Tot Nook.

L' Tot Nook is a baby boutique which sells only handmade clothing and accessories for both boys and girls. Our store will live exclusively online.

We would like to only use the colors that have been used in the logo.

Target Market(s)

Potential wholesale clients, Small business owners

Industry/Entity Type

Retail

Contact Information for Business Card

Name Wendell R. Fauste (Owner)
Email sales@ltotnook.example
Main Phone 555-013-2947
Cell phone 555-013-6152
Website www.LTotNook.example

Font styles to use
Sans Serif

Colors

Designer to choose colors to be used in the design.

Requirements
Must have
• -Would like to have icons that indentify the contact information.
• -Include our website
• -Include our tagline in a small area near the bottom. "Handmade Baby Creations"
• -Would like to include Facebook and Instagram Icons
• -
Nice to have
• Would like to have a simple back side with the logo.
• Something along the lines of the marlow ridge card attached.

```html
<!DOCTYPE html>
<html lang="en">
<head>
<meta charset="utf-8">
<title>L' Tot Nook – Business Card</title>
<link href="https://fonts.googleapis.com/css2?family=Roboto:wght@400;500&display=swap" rel="stylesheet">
<style>
  :root {
    --bg: #f4f4f4;
    --card-dark: #121212;
    --card-glow: #2b2b2b;
    --mint: #74cfbb;
    --coral: #e9655d;
    --ink: #1a1a1a;
  }
  * { box-sizing: border-box; margin: 0; padding: 0; }
  html, body { width: 1200px; height: 900px; overflow: hidden; }
  body {
    background: var(--bg);
    font-family: "Roboto", Arial, sans-serif;
    display: flex;
    align-items: center;
    justify-content: center;
    gap: 40px;
  }
  .card {
    position: relative;
    width: 560px;
    height: 320px;
    border-radius: 26px;
    overflow: hidden;
    background: radial-gradient(ellipse at 45% 40%, var(--card-glow) 0%, var(--card-dark) 70%);
    box-shadow: 0 18px 30px rgba(0,0,0,0.18);
  }
  .brand-name {
    color: var(--mint);
    font-weight: 500;
    font-size: 50px;
    line-height: 1;
    letter-spacing: 0.5px;
    white-space: nowrap;
  }

  /* Back side */
  .card-back { display: flex; flex-direction: column; align-items: center; justify-content: center; }
  .card-back .brand-name { margin-top: 10px; font-size: 56px; }
  .social { display: flex; gap: 12px; margin-top: 70px; }
  .social-dot { width: 20px; height: 20px; border-radius: 50%; background: var(--coral); }

  /* Front side */
  .card-front .brand-name { position: absolute; left: 42px; top: 112px; font-size: 46px; }
  .person { position: absolute; left: 312px; top: 52px; }
  .person-name { color: var(--coral); font-size: 17px; font-weight: 500; }
  .person-role { color: var(--mint); font-size: 12px; margin-top: 3px; }
  .contact-list { position: absolute; left: 312px; top: 122px; list-style: none; }
  .contact-item { display: flex; align-items: center; gap: 9px; height: 23px; color: var(--mint); font-size: 12.5px; }
  .contact-icon { width: 15px; height: 15px; border-radius: 50%; background: var(--coral); display: flex; align-items: center; justify-content: center; flex: none; }
  .contact-icon svg { width: 9px; height: 9px; }
  .tagline-band {
    position: absolute; left: 0; right: 0; bottom: 0; height: 30px;
    background: var(--mint);
    border-top: 4px solid var(--coral);
    display: flex; align-items: center; justify-content: center;
    color: var(--ink); font-size: 11px; font-weight: 500; letter-spacing: 9px;
  }
</style>
</head>
<body>

  <section class="card card-back" aria-label="Card back">
    <div class="brand-name">L' Tot Nook</div>
    <div class="social" aria-label="Social media">
      <span class="social-dot"></span>
      <span class="social-dot"></span>
    </div>
  </section>

  <section class="card card-front" aria-label="Card front">
    <div class="brand-name">L' Tot Nook</div>

    <div class="person">
      <div class="person-name">Wendell R. Fauste</div>
      <div class="person-role">Owner</div>
    </div>

    <ul class="contact-list">
      <li class="contact-item">
        <span class="contact-icon"><svg viewBox="0 0 10 10"><path d="M2 1 L4 1 L4.6 3 L3.6 3.8 Q4.6 5.6 6.2 6.4 L7 5.4 L9 6 L9 8 Q5 9 2.5 6 Q1 4 2 1Z" fill="#121212"/></svg></span>
        555-013-2947
      </li>
      <li class="contact-item">
        <span class="contact-icon"><svg viewBox="0 0 10 10"><rect x="3" y="1" width="4" height="8" rx="0.8" fill="none" stroke="#121212" stroke-width="1.2"/><circle cx="5" cy="7.4" r="0.5" fill="#121212"/></svg></span>
        555-013-6152
      </li>
      <li class="contact-item">
        <span class="contact-icon"><svg viewBox="0 0 10 10"><rect x="1" y="2.5" width="8" height="5.5" fill="#121212"/><path d="M1 2.5 L5 5.5 L9 2.5" fill="none" stroke="#e9655d" stroke-width="0.8"/></svg></span>
        sales@ltotnook.example
      </li>
      <li class="contact-item">
        <span class="contact-icon"><svg viewBox="0 0 10 10" fill="none" stroke="#121212" stroke-width="0.9"><circle cx="5" cy="5" r="3.8"/><ellipse cx="5" cy="5" rx="1.6" ry="3.8"/><path d="M1.2 5 H8.8"/></svg></span>
        www.LTotNook.example
      </li>
    </ul>

    <div class="tagline-band">Handmade Baby Creations</div>
  </section>

</body>
</html>
```